M&A Advisory firm needs elegant and powerful letterhead

We need a powerful but elegant letterhead to engage with the international financial industry.

Target Market(s)

New York and International Financial Industry

Industry/Entity Type

Finance

Font styles to use
Other font styles liked:
• Poppins

Requirements
Must have
• 482 W 71st Street 14th Floor New York, NY 10157 O: +1 (212) 555 0147 F: +1 (212) 555 0182

```html
<!DOCTYPE html>
<html lang="en">
<head>
<meta charset="utf-8">
<title>Halden Partners Letterhead</title>
<link href="https://fonts.googleapis.com/css2?family=Poppins:wght@300;400;500&display=swap" rel="stylesheet">
<style>
  :root {
    --backdrop: #d9d9d9;
    --paper: #fafafa;
    --navy: #1a4a7c;
    --navy-deep: #123a66;
    --ink: #5a5a5a;
    --ink-dark: #2f2f2f;
    --sign-fill: #e3e7ef;
  }
  * { margin: 0; padding: 0; box-sizing: border-box; }
  html, body {
    width: 1200px; height: 960px; overflow: hidden;
    background: var(--backdrop);
    font-family: "Poppins", sans-serif;
  }
  .letterhead {
    position: absolute; left: 270px; top: 13px;
    width: 660px; height: 934px;
    background: var(--paper);
    box-shadow: 0 6px 24px rgba(0,0,0,0.12);
    color: var(--ink);
    overflow: hidden;
  }
  .top-band {
    height: 18px;
    background: linear-gradient(90deg, var(--navy), var(--navy-deep));
  }
  .brand {
    display: flex; align-items: center; justify-content: center; gap: 12px;
    margin-top: 42px;
  }
  .brand-dot {
    width: 22px; height: 22px; border-radius: 50%;
    background: var(--navy);
  }
  .brand-name {
    font-size: 28px; font-weight: 400; color: var(--navy);
    letter-spacing: 0.5px;
  }
  .letter-body {
    position: absolute; left: 72px; right: 72px; top: 250px;
    font-size: 9.6px; line-height: 1.65; font-weight: 300;
  }
  .recipient { margin-bottom: 14px; }
  .salutation {
    font-size: 11px; font-weight: 400; color: var(--ink-dark);
    margin-bottom: 10px;
  }
  .letter-body p.para { margin-bottom: 18px; }
  .closing { margin-top: 24px; }
  .signature {
    display: block; width: 130px; height: 34px;
    margin: 12px 0 8px; background: var(--sign-fill); border-radius: 3px;
  }
  .signer-name { font-size: 10.5px; font-weight: 400; color: var(--ink-dark); }
  .signer-role { font-size: 9px; }
  .contact {
    position: absolute; left: 150px; bottom: 40px;
    font-size: 12px; color: var(--ink); line-height: 1.5;
  }
  .contact-line { display: flex; align-items: center; gap: 8px; }
  .bullet {
    width: 5px; height: 5px; border-radius: 50%;
    background: var(--navy); flex: none;
  }
  .contact-gap { margin-left: 10px; }
</style>
</head>
<body>
  <main class="letterhead">
    <div class="top-band"></div>

    <header class="brand">
      <span class="brand-dot"></span>
      <span class="brand-name">Halden Partners</span>
    </header>

    <section class="letter-body">
      <div class="recipient">
        Mr. Lorem ipsum<br>President<br>Company Name<br>Location here
      </div>
      <div class="salutation">Dear Mr. Lorem ipsum</div>

      <p class="para">Lorem ipsum dolor sit amet, consectetuer adipiscing elit, sed diam nonummy nibh euismod tincidunt ut laoreet dolore magna aliquam erat volutpat. Ut wisi enim ad minim veniam, quis nostrud exerci tation ullamcorper suscipit lobortis nisl ut aliquip ex ea commodo consequat. Duis autem vel eum iriure dolor in hendrerit in vulputate velit esse molestie consequat, vel illum dolore eu feugiat nulla facilisis at vero eros et accumsan et iusto odio dignissim qui blandit praesent luptatum zzril delenit augue duis dolore te feugait nulla facilisi.</p>

      <p class="para">Lorem ipsum dolor sit amet, cons ectetuer adipiscing elit, sed diam nonummy nibh euismod tincidunt ut laoreet dolore magna aliquam erat volutpat. Ut wisi enim ad minim veniam, quis nostrud exerci tation ullamcorper suscipit lobortis nisl ut aliquip ex ea commodo consequat.</p>

      <p class="para">Lorem ipsum dolor sit amet, consectetuer adipiscing elit, sed diam nonummy nibh euismod tincidunt ut laoreet dolore magna aliquam erat volutpat. Ut wisi enim ad minim veniam, quis nostrud exerci tation ullamcorper suscipit lobortis nisl ut aliquip ex ea commodo consequat. Duis autem vel eum iriure dolor in hendrerit in vulputate velit esse molestie consequat, vel illum dolore eu feugiat nulla facilisis at vero eros et accumsan et iusto odio dignissim qui blandit praesent luptatum zzril delenit augue duis dolore te feugait nulla facilisi.</p>

      <p class="para">Lorem ipsum dolor sit amet, cons ectetuer adipiscing elit, sed diam nonummy nibh euismod tincidunt ut laoreet dolore magna aliquam erat volutpat. Ut wisi enim ad minim veniam, quis nostrud exerci tation ullamcorper suscipit lobortis nisl ut aliquip ex ea commodo consequat.</p>

      <div class="closing">
        Yours sincerely,
        <span class="signature" role="img" aria-label="Handwritten signature"></span>
        <div class="signer-name">Lorem ipsum</div>
        <div class="signer-role">Chairmen</div>
      </div>
    </section>

    <footer class="contact">
      <div class="contact-line">
        <span class="bullet"></span><span>O: +1 (212) 555 0147</span>
        <span class="bullet contact-gap"></span><span>F: +1 (212) 555 0182</span>
      </div>
      <div class="contact-line">
        <span class="bullet"></span><span>482 W 71st Street 14th Floor New York, NY 10157</span>
      </div>
    </footer>
  </main>
</body>
</html>
```